Nail salon window signage design

We need new signage to be designed for our existing nail salon. The sign will be a large sticker that will stick onto the glass window at the front.

Some of the services we provide are:
Manicures
Pedicures
Velora Gel Builder
Acrylic Nails
KVT
Brenlux
Gel Polish
You may wish to have our services listed on the sign but is not compulsory.

I have also attached our logo which can be used on the sign but is not compulsory.

I have also attached a photo of the front of our salon and the sign will be where I have outlined in yellow.

The size of the sign will be 119cm wide and 170cm high.

I am open to any nice classy design you can think of.

```html
<!DOCTYPE html>
<html lang="en">
<head>
<meta charset="utf-8">
<title>Aurelia Nails – Services</title>
<link rel="stylesheet" href="https://fonts.googleapis.com/css2?family=Libre+Baskerville&family=Playfair+Display:ital,wght@1,900&display=swap">
<style>
  :root {
    --paper: #fcf6f3;
    --wine: #8f1d2e;
    --navy: #1f1a4f;
    --skin-light: #f6c9b3;
    --skin-deep: #eeb49c;
    --lacquer: #c22a3a;
  }
  html, body {
    margin: 0;
    padding: 0;
    overflow: hidden;
    background: #ffffff;
  }
  .sign {
    position: relative;
    width: 840px;
    height: 1200px;
    overflow: hidden;
    background:
      radial-gradient(ellipse 260px 420px at 40px 330px, rgba(242, 190, 190, 0.55), transparent 70%),
      radial-gradient(ellipse 220px 300px at 820px 680px, rgba(246, 205, 210, 0.45), transparent 70%),
      radial-gradient(ellipse 300px 160px at 690px 70px, rgba(240, 222, 180, 0.35), transparent 70%),
      var(--paper);
  }
  .brand {
    position: absolute;
    top: 188px;
    left: 0;
    width: 100%;
    margin: 0;
    text-align: center;
    font-family: "Libre Baskerville", Georgia, serif;
    font-weight: 400;
    font-size: 86px;
    line-height: 1;
    color: var(--wine);
  }
  .services-title {
    position: absolute;
    top: 392px;
    left: 0;
    width: 100%;
    margin: 0;
    text-align: center;
    font-family: "Playfair Display", Georgia, serif;
    font-style: italic;
    font-weight: 900;
    font-size: 66px;
    line-height: 1;
    color: var(--navy);
  }
  .services-list {
    position: absolute;
    top: 482px;
    left: 0;
    width: 100%;
    margin: 0;
    padding: 0;
    list-style: none;
    text-align: center;
    font-family: "Libre Baskerville", Georgia, serif;
    font-size: 37px;
    line-height: 68px;
    color: var(--navy);
    z-index: 2;
  }
  .nail-art {
    position: absolute;
    left: 0;
    top: 880px;
    width: 840px;
    height: 320px;
    z-index: 1;
  }
</style>
</head>
<body>
  <main class="sign">
    <h1 class="brand">Aurelia Nails</h1>
    <h2 class="services-title">services list</h2>
    <ul class="services-list">
      <li>Velora Gel Builder</li>
      <li>Acrylic Nails</li>
      <li>Manicures</li>
      <li>Gel Polish</li>
      <li>Pedicures</li>
      <li>Brenlux</li>
      <li>KVT</li>
    </ul>
    <svg class="nail-art" viewBox="0 0 840 320" role="img" aria-label="Illustration of six fingertips with red lacquered nails in different shapes: slanted, square, stiletto, almond, flared and oval">
      <defs>
        <linearGradient id="nail-art-fill" x1="0" y1="0" x2="0" y2="1">
          <stop offset="0" stop-color="#c22a3a" stop-opacity="0.8"/>
          <stop offset="0.4" stop-color="#e79c8f"/>
          <stop offset="0.6" stop-color="#f6c9b3"/>
          <stop offset="1" stop-color="#eeb49c"/>
        </linearGradient>
      </defs>
      <path d="M48 320 V60 Q48 24 84 24 H300 Q330 24 340 70 Q350 105 380 105 H460 Q490 105 500 70 Q510 10 560 10 H756 Q792 10 792 46 V320 Z" fill="url(#nail-art-fill)"/>
    </svg>
  </main>
</body>
</html>
```